" Somos uma empresa de pintura residencial profissional que utiliza novos equipamentos e processos para satisfazer o desejo do nosso cliente: tempo de execução adequado, limpeza e custo "

```html
<!DOCTYPE html>
<html lang="pt-BR">
<head>
<meta charset="utf-8">
<title>Lumera Pintura – Cartão de visita</title>
<link rel="stylesheet" href="https://fonts.googleapis.com/css2?family=Arimo:wght@400;700&display=swap">
<style>
  :root {
    --backdrop: #e6e6e4;
    --card-dark: #262626;
    --card-light: #ffffff;
    --accent: #f07d16;
    --ink: #1e1e1e;
    --ink-soft: #444444;
    --ghost: #f1f1f1;
  }
  * { box-sizing: border-box; margin: 0; padding: 0; }
  html, body {
    width: 1200px; height: 1200px; overflow: hidden;
    background: var(--backdrop);
    font-family: "Arimo", Arial, sans-serif;
  }
  .sheet {
    position: relative; width: 1200px; height: 1200px;
  }
  .card {
    position: absolute; left: 180px; width: 840px; height: 480px;
    box-shadow: 0 10px 30px rgba(0,0,0,.18);
    overflow: hidden;
  }
  .card--front { top: 90px; background: var(--card-dark); }
  .card--back  { top: 630px; background: var(--card-light); }

  .front-stripe {
    position: absolute; left: 0; top: 0; bottom: 0; width: 26px;
    background: var(--accent);
  }
  .brand {
    display: flex; align-items: center; gap: 16px;
    font-weight: 700; letter-spacing: 2px; white-space: nowrap;
  }
  .brand-mark { width: 30px; height: 30px; background: var(--accent); flex: none; }
  .card--front .brand {
    position: absolute; left: 50%; top: 50%;
    transform: translate(-50%, -50%);
    color: #ffffff; font-size: 58px;
  }
  .card--front .brand-mark { width: 44px; height: 44px; }

  .back-ghost {
    position: absolute; left: 300px; top: 120px; width: 300px; height: 300px;
    background: radial-gradient(circle at 50% 50%, var(--ghost) 0%, rgba(241,241,241,0) 70%);
  }
  .card--back .brand {
    position: absolute; left: 60px; top: 70px;
    color: var(--ink); font-size: 40px;
  }
  .person {
    position: absolute; left: 60px; top: 200px; color: var(--ink);
  }
  .person-name { font-size: 28px; }
  .person-role { font-size: 18px; color: var(--ink-soft); margin-top: 8px; }
  .contact {
    position: absolute; right: 90px; top: 260px;
    text-align: right; font-size: 20px; line-height: 1.35; color: var(--ink);
  }
  .contact-web { font-weight: 700; }
  .back-tab {
    position: absolute; right: 0; bottom: 40px; width: 22px; height: 150px;
    background: linear-gradient(to bottom, var(--accent) 0 62%, var(--card-dark) 62% 100%);
  }
</style>
</head>
<body>
<main class="sheet">
  <section class="card card--front" aria-label="Frente do cartão">
    <div class="front-stripe"></div>
    <div class="brand"><span class="brand-mark"></span>LUMERA PINTURA</div>
  </section>

  <section class="card card--back" aria-label="Verso do cartão">
    <div class="back-ghost" role="img" aria-label="Símbolo decorativo da marca em tom claro"></div>
    <div class="brand"><span class="brand-mark"></span>LUMERA PINTURA</div>
    <div class="person">
      <p class="person-name">Nome Sobrenome</p>
      <p class="person-role">Cargo</p>
    </div>
    <address class="contact" style="font-style:normal">
      <p>Rua do Projeto, 000 - Centro</p>
      <p>81 0000-0000</p>
      <p>contato@lumera.com.br</p>
      <p class="contact-web">www.lumera.com.br</p>
    </address>
    <div class="back-tab"></div>
  </section>
</main>
</body>
</html>
```